Web Design Project

Looking for a web page design for a consulting company called Tessaro Consulting.

Tessaro specialize in Business Improvement and Transformation consulting in the Mining, Infrastructure, Logistics and Transport sectors.
Updates

Industry/Entity Type

Business

Font styles to use
Sans Serif

Colors
86cae7
0892cd
ecf7f5

```html
<!DOCTYPE html>
<html lang="en">
<head>
<meta charset="utf-8">
<title>Tessaro Consulting</title>
<link rel="stylesheet" href="https://fonts.googleapis.com/css2?family=Open+Sans:wght@400;600&display=swap">
<style>
  :root {
    --sky: #86cae7;
    --blue: #0892cd;
    --mist: #ecf7f5;
    --nav-top: #8ec3ea;
    --nav-mid: #5a9fd8;
    --nav-bot: #3f86c7;
    --nav-active: #7cb6e6;
    --heading: #3d8fd2;
    --ink: #333b44;
    --logo: #4a5560;
    --panel: #fbfcfc;
    --footer: #f4f5f5;
  }
  * { box-sizing: border-box; margin: 0; padding: 0; }
  html, body { width: 998px; height: 1200px; overflow: hidden; background: #fff; }
  body { position: relative; font-family: "Open Sans", Arial, sans-serif; color: var(--ink); }

  .brand { position: absolute; left: 132px; top: 40px; width: 180px; text-align: center; }
  .brand-dot { display: block; width: 70px; height: 70px; border-radius: 50%; background: var(--blue); margin: 0 auto 14px; }
  .brand-name { display: block; font-size: 29px; letter-spacing: 5px; color: var(--logo); font-weight: 400; line-height: 1; }
  .brand-sub { display: block; font-size: 12px; letter-spacing: 4px; color: var(--logo); font-weight: 400; margin-top: 4px; }

  .main-nav { position: absolute; left: 90px; top: 195px; width: 856px; height: 45px; border-radius: 6px 6px 0 0;
    background: linear-gradient(var(--nav-top), var(--nav-mid) 55%, var(--nav-bot)); box-shadow: 0 3px 4px rgba(0,0,0,.35); }
  .nav-item { position: absolute; top: 0; height: 45px; display: flex; align-items: center; justify-content: center;
    color: #fff; font-size: 15px; letter-spacing: 1.5px; border-right: 1px solid rgba(255,255,255,.35); }
  .nav-item.is-active { background: linear-gradient(#a6d1f1, var(--nav-active) 60%, #5d9fd8); }
  .search { position: absolute; left: 610px; top: 10px; width: 228px; height: 25px; border-radius: 3px;
    background: linear-gradient(#9ccaf0, #4f93d4); border: 1px solid #d6e9f8; }
  .search span { position: absolute; left: 19px; top: 4px; font-size: 11px; color: #e8f3fc; letter-spacing: 1px; }
  .search-btn { position: absolute; right: 0; top: 0; width: 25px; height: 23px; background: #fff; display: flex; align-items: center; justify-content: center; }

  .hero { position: absolute; left: 88px; top: 240px; width: 852px; height: 374px;
    background: linear-gradient(160deg, #6f9fd8 0%, #3f78c0 35%, #c98a5e 55%, #a7a9ad 75%, #d6c7ac 100%); }
  .hero-globe { position: absolute; right: 2px; top: 2px; width: 370px; height: 370px; border-radius: 50%;
    background: radial-gradient(circle at 60% 35%, #bcd6f3, #6e9ed9 55%, #3e73bf); opacity: .85; }
  .hero-title { position: absolute; left: 22px; top: 88px; color: #fff; font-size: 27px; font-weight: 600;
    letter-spacing: 3px; line-height: 45px; text-shadow: 2px 2px 3px rgba(0,0,0,.7); }

  .sector { position: absolute; top: 631px; height: 158px; }
  .sector-tab { height: 35px; border-radius: 4px 4px 0 0; background: linear-gradient(#a5cdef, #5d9dd6);
    color: #fff; font-size: 17px; letter-spacing: 2px; text-align: center; line-height: 35px; }
  .sector-photo { height: 123px; }
  .sector::after { content: ""; position: absolute; left: 8%; right: 8%; bottom: -12px; height: 12px;
    background: radial-gradient(ellipse at top, rgba(0,0,0,.35), transparent 70%); }

  .service { position: absolute; background: var(--panel); box-shadow: 0 0 3px rgba(0,0,0,.03); }
  .service h2 { font-weight: 400; font-size: 15px; color: var(--heading); letter-spacing: 1.5px; }
  .service p { font-size: 11.5px; letter-spacing: 1px; line-height: 12.6px; margin-top: 10px; }

  .footer { position: absolute; left: 83px; top: 1076px; width: 857px; height: 87px; background: var(--footer); }
  .footer small { position: absolute; left: 15px; top: 64px; font-size: 9.5px; letter-spacing: 1px; color: var(--ink); }
  .social { position: absolute; right: 15px; top: 55px; display: flex; gap: 7px; }
  .social i { width: 22px; height: 22px; border-radius: 2px; display: block; }
</style>
</head>
<body>
  <header>
    <div class="brand">
      <span class="brand-dot"></span>
      <span class="brand-name">TESSARO</span>
      <span class="brand-sub">CONSULTING</span>
    </div>

    <nav class="main-nav">
      <a class="nav-item" style="left:0;width:145px">HOME</a>
      <a class="nav-item" style="left:145px;width:151px">ABOUT US</a>
      <a class="nav-item is-active" style="left:296px;width:150px">SERVICES</a>
      <a class="nav-item" style="left:446px;width:150px">CONTACT</a>
      <div class="search">
        <span>Search</span>
        <div class="search-btn">
          <svg width="14" height="14" viewBox="0 0 14 14"><circle cx="5.5" cy="5.5" r="4" fill="none" stroke="#2f7bc4" stroke-width="2"/><line x1="8.5" y1="8.5" x2="13" y2="13" stroke="#2f7bc4" stroke-width="2.5"/></svg>
        </div>
      </div>
    </nav>
  </header>

  <section class="hero" role="img" aria-label="Construction worker on steel reinforcement with a glass globe">
    <div class="hero-globe"></div>
    <h1 class="hero-title">BUSINESS IMPROVEMENT<br>TRANSFORMATION CONSULTING</h1>
  </section>

  <section>
    <div class="sector" style="left:101px;width:190px">
      <div class="sector-tab">Mining</div>
      <div class="sector-photo" role="img" aria-label="Mining excavator at a quarry under blue sky" style="background:linear-gradient(#5d8fd4,#b9c9dc 45%,#a89b86)"></div>
    </div>
    <div class="sector" style="left:312px;width:186px">
      <div class="sector-tab">Infrastructure</div>
      <div class="sector-photo" role="img" aria-label="Aerial view of a highway interchange" style="background:linear-gradient(135deg,#6f8f5a,#b8bcb8 50%,#5f8a4c)"></div>
    </div>
    <div class="sector" style="left:518px;width:189px">
      <div class="sector-tab">Transport</div>
      <div class="sector-photo" role="img" aria-label="Red truck on a motorway" style="background:linear-gradient(#6d9a46,#8c9396 55%,#7b8285)"></div>
    </div>
    <div class="sector" style="left:728px;width:190px">
      <div class="sector-tab">Logistics</div>
      <div class="sector-photo" role="img" aria-label="Warehouse with stocked pallet racks" style="background:linear-gradient(90deg,#4d6fb4,#c49a6c 50%,#4d6fb4)"></div>
    </div>
  </section>

  <section>
    <article class="service" style="left:133px;top:855px;width:326px;height:156px;padding:12px 14px">
      <h2 style="padding-left:5px">SERVICES</h2>
      <p>We provide performance measurement to monitor and record the improvement to the Construction Environment brought about by the development of Partnering Procurement and Total Quality Management.</p>
    </article>
    <article class="service" style="left:570px;top:853px;width:327px;height:152px;padding:18px 30px">
      <h2 style="margin-left:3px">SERVICES</h2>
      <p style="margin-top:14px">We specialise in finding expert candidates for sought after roles with the best companies in the country. Got some skills? Looking for the right candidate?</p>
    </article>
  </section>

  <footer class="footer">
    <small>2013 TESSARO Consulting , All Rights REserved.</small>
    <div class="social">
      <i style="background:#3b5998"></i>
      <i style="background:#55acee"></i>
      <i style="background:#0e76a8"></i>
      <i style="background:#f26f21"></i>
    </div>
  </footer>
</body>
</html>
```